Simple : A Therapist is looking for a Design

Im lookind for a business card design for my new business .
my therapy field - Attuned Somatic Release .
Its part of Osteopatic medicine .
its gental, not invasive method that focus on the bones of the skull (cranial) .
i want some kind of skull in it like the attached photo.

Target Market(s)

people that suffer from pain

Industry/Entity Type

Physical Therapy

Contact Information for Business Card

i want people to understand this is diffrent kind of therapy
its anatomy base , gental and give outstanding result .

Font styles to use
Serif

Colors
fee18a
cadf82
fbc994
cedeed
fbe7d2
fff3d1

Requirements
Must have
• one side: my name (Eliran Tsabari) ,
• phone number ( 0541762908)
• email (tsabarieliran@mailvent.net)
• other side : Attuned Somatic Release
Nice to have
• i want some kind of skull in it like the attached photo.
• very powrful, accurate and smart.
• nice colores (maybe lite orange?, lite green?) , simple, relax, smart

```html
<!DOCTYPE html>
<html lang="en">
<head>
<meta charset="utf-8">
<title>Eliran Tsabari — Business Card</title>
<link href="https://fonts.googleapis.com/css2?family=Josefin+Sans:wght@300;400;700&display=swap" rel="stylesheet">
<style>
  :root {
    --backdrop: #ecebe8;
    --card-green: #cadf82;
    --card-yellow: #fee18a;
    --frost: rgba(255, 255, 255, 0.72);
    --ink-white: #ffffff;
    --ink-grey: #7d7d7d;
    --accent-dot: #fee18a;
  }
  * { margin: 0; padding: 0; box-sizing: border-box; }
  html, body {
    width: 1200px;
    height: 900px;
    overflow: hidden;
    background: var(--backdrop);
    font-family: "Josefin Sans", sans-serif;
  }
  .business-card {
    position: absolute;
    left: 150px;
    top: 172px;
    width: 900px;
    height: 557px;
    background: linear-gradient(to right, var(--card-green) 0 607px, var(--card-yellow) 607px 100%);
    overflow: hidden;
    box-shadow: 0 10px 30px rgba(0, 0, 0, 0.12);
  }
  .holder-name {
    position: absolute;
    left: 55px;
    top: 64px;
    color: var(--ink-white);
    font-weight: 700;
    font-size: 29px;
    letter-spacing: 1.5px;
    text-transform: uppercase;
  }
  .contact-list {
    position: absolute;
    left: 55px;
    top: 420px;
    list-style: none;
    color: var(--ink-white);
    font-weight: 400;
    font-size: 25px;
  }
  .contact-item {
    display: flex;
    align-items: center;
    gap: 10px;
    height: 37px;
  }
  .contact-icon { width: 22px; height: 22px; fill: var(--ink-white); flex: none; }
  .brand-disc {
    position: absolute;
    left: 372px;
    top: 41px;
    width: 476px;
    height: 476px;
    border-radius: 50%;
    background: var(--frost);
    display: flex;
    flex-direction: column;
    align-items: center;
    justify-content: center;
    gap: 34px;
  }
  .brand-dot {
    width: 120px;
    height: 120px;
    border-radius: 50%;
    background: var(--accent-dot);
  }
  .brand-name {
    color: var(--ink-grey);
    font-weight: 400;
    font-size: 33px;
    letter-spacing: 1px;
    white-space: nowrap;
  }
</style>
</head>
<body>
  <main class="business-card">
    <h1 class="holder-name">Eliran Tsabari</h1>

    <ul class="contact-list">
      <li class="contact-item">
        <svg class="contact-icon" viewBox="0 0 24 24" aria-hidden="true">
          <path d="M3 9c0-3 4-5 9-5s9 2 9 5v1.5h-4.5V8.5c-1.5-.6-3-.8-4.5-.8s-3 .2-4.5.8v2H3z"/>
          <path d="M7 11h10l3 6v3H4v-3zM12 13.2a2.6 2.6 0 1 0 0 5.2 2.6 2.6 0 0 0 0-5.2z"/>
        </svg>
        <span>0541762908</span>
      </li>
      <li class="contact-item">
        <svg class="contact-icon" viewBox="0 0 24 24" aria-hidden="true">
          <path d="M2 5h20v14H2zM3.5 6.5 12 13l8.5-6.5" fill="none" stroke="#fff" stroke-width="0"/>
          <path d="M2 5h20v1.4l-10 7.2L2 6.4zM2 8.4l10 7.2 10-7.2V19H2z"/>
        </svg>
        <span>tsabarieliran@mailvent.net</span>
      </li>
    </ul>

    <div class="brand-disc">
      <div class="brand-dot"></div>
      <p class="brand-name">Attuned Somatic Release</p>
    </div>
  </main>
</body>
</html>
```